HR Technology Company (Corvinex) needs a consistent powerpoint deck for future presentations

We are Corvinex (corvinex-example.com). You can visit our website for colours scheme etc. I am looking for a full PPT pack which can be used for various presentations in the future. Sales Presentation, Company Overview etc. This must include charts, graphs, services (4/6/8 items), people slide, timeline slides etc among all the other common slides.

```html
<!DOCTYPE html>
<html lang="en">
<head>
<meta charset="utf-8">
<title>Corvinex Presentation Pack</title>
<link href="https://fonts.googleapis.com/css2?family=Lato:wght@400;700;900&display=swap" rel="stylesheet">
<style>
:root{
  --orange:#f7941d;
  --orange-deep:#ef7d00;
  --gold:#f5b400;
  --ink:#222222;
  --grey:#6b6b6b;
  --line:#e3e3e3;
  --band:#2a2a2a;
  --paper:#ffffff;
  --photo-a:#c7a283;
  --photo-b:#6e5c4d;
}
*{box-sizing:border-box;margin:0;padding:0}
html,body{width:1200px;height:1200px;overflow:hidden;background:var(--paper);font-family:'Lato',sans-serif;color:var(--ink)}
.deck{display:grid;grid-template-columns:repeat(5,207px);grid-auto-rows:116px;gap:28px 26px;padding:35px 0 0 29px}
.slide{position:relative;width:207px;height:116px;background:var(--paper);box-shadow:0 2px 6px rgba(0,0,0,.28);overflow:hidden}
.slide > *{position:absolute}
.footer{left:0;right:0;bottom:0;height:4px;background:var(--band);display:flex;justify-content:space-between;align-items:center;padding:0 5px;font-size:2.2px;color:#ddd}
.footer .site{color:var(--orange)}
.brand{top:6px;right:7px;display:flex;align-items:center;gap:1.5px;font-size:4.6px;font-weight:700;color:var(--ink)}
.brand::before{content:"";width:3px;height:3px;background:var(--orange)}
.brand.light{color:#fff}
.title{left:15px;top:14px;font-size:7px;font-weight:700;color:var(--ink);white-space:nowrap}
.title.center{left:0;right:0;text-align:center}
.accent{color:var(--orange)}
.kicker{left:15px;top:0;right:0;font-size:1.8px;color:var(--grey);letter-spacing:.1px}
.sub{font-size:3.2px;font-weight:700;color:var(--ink)}
.body{font-size:2.2px;line-height:1.35;color:var(--grey)}
.photo{background:linear-gradient(135deg,var(--photo-a),var(--photo-b))}
.photo.warm{background:linear-gradient(135deg,#d9b48d,#7a6150)}
.photo.cool{background:linear-gradient(135deg,#b9b2a8,#5c5650)}
.card{background:#fff;border:0.5px solid var(--line);box-shadow:0 1px 2px rgba(0,0,0,.12);display:flex;flex-direction:column;align-items:center;padding:4px 2px;text-align:center;gap:2px}
.card .icon{width:6px;height:6px;border:0.7px solid var(--ink);border-radius:50%}
.card .name{font-size:2.4px;font-weight:700}
.card .body{font-size:1.8px}
.dot{width:7px;height:7px;border-radius:50%;display:flex;align-items:center;justify-content:center;color:#fff;font-size:4px}
.dot.orange{background:var(--orange)}
.dot.dark{background:var(--ink)}
.dot.grey{background:#8a8a8a}
.bullet-row{display:flex;gap:4px;align-items:flex-start}
.bullet-row .label{font-size:2.6px;color:var(--orange);font-weight:700}
.bullet-row .label.muted{color:var(--grey)}
.orange-panel{background:var(--orange);color:#fff}
.cover-title{font-size:6px;color:#fff;line-height:1.15}
.logo-big{display:flex;align-items:center;gap:3px;font-weight:900;color:var(--ink)}
.logo-big::before{content:"";width:7px;height:7px;background:var(--orange-deep)}
.tagline{font-size:3.6px;color:var(--ink)}
.badge{width:17px;height:11px;background:#fff;border-radius:1px}
.col-head{font-size:2.5px;font-weight:700;border-top:1px solid var(--orange);padding-top:2px}
.ring{width:22px;height:22px;border-radius:50%;display:flex;align-items:center;justify-content:center;font-size:4px}
table.grid{border-collapse:collapse;font-size:1.9px;color:var(--grey)}
table.grid th{background:var(--orange);color:#fff;font-weight:700;padding:0.6px 2px}
table.grid td{border-bottom:0.3px solid var(--line);padding:0.5px 2px;text-align:center}
table.grid td:first-child{text-align:left}
</style>
</head>
<body>
<main class="deck">

<!-- Row 1: covers and agenda -->
<section class="slide">
  <div class="photo" role="img" aria-label="Photo of a smiling woman at a laptop" style="inset:0;background:linear-gradient(90deg,#f39a1c 0,#f5b24a 42%,#bba58c 62%,#76695c 100%)"></div>
  <div style="left:11px;top:22px;width:76px;height:75px;background:rgba(247,148,29,.85)"></div>
  <div class="logo-big" style="left:16px;top:28px;font-size:12px">Corvinex</div>
  <div class="tagline" style="left:23px;top:44px">People Strategy, Redefined</div>
  <div class="cover-title" style="left:23px;top:57px;width:60px;border-left:0.7px solid #fff;padding-left:2px">Click to include your title presentation here</div>
  <div class="body" style="left:20px;top:88px;color:#fff">Your Subtitle Presentation goes here</div>
  <div class="badge" style="right:9px;bottom:14px"></div>
</section>

<section class="slide">
  <div class="photo" role="img" aria-label="Photo of a smiling woman at a laptop" style="inset:0;background:linear-gradient(90deg,#f7d08a 0,#f3b552 40%,#b59f86 65%,#6f6358)"></div>
  <div class="logo-big" style="left:18px;top:26px;font-size:12px">Corvinex</div>
  <div class="tagline" style="left:24px;top:42px">People Strategy, Redefined</div>
  <div style="left:18px;top:60px;font-size:5.5px;color:var(--ink);line-height:1.2">Click to include your<br><b>title presentation here</b></div>
  <div class="body" style="left:18px;top:78px;color:var(--ink)">Your Subtitle Presentation goes here</div>
  <div style="left:40px;top:86px;display:flex;gap:2px"><i style="width:3px;height:3px;border:0.4px solid #fff"></i><i style="width:3px;height:3px;border:0.4px solid #fff"></i><i style="width:3px;height:3px;border:0.4px solid #fff"></i></div>
  <div class="badge" style="right:9px;bottom:14px"></div>
</section>

<section class="slide">
  <div class="photo cool" role="img" aria-label="Photo of a team reviewing work on a laptop" style="left:0;top:0;width:207px;height:75px;background:linear-gradient(90deg,#fff 0,#fff 30%,#c9c1b8 45%,#7c7168)"></div>
  <div class="logo-big" style="left:6px;top:18px;font-size:13px">Corvinex</div>
  <div class="tagline" style="left:10px;top:36px;font-size:4.4px">People Strategy, Redefined</div>
  <div class="badge" style="left:72px;top:44px;width:12px;height:8px;background:var(--gold)"></div>
  <div style="left:0;right:0;top:80px;text-align:center;font-size:5.5px;color:var(--orange)">Click to include your Title Presentation</div>
  <div class="body" style="left:0;right:0;top:89px;text-align:center;color:var(--ink)">Your Subtitle Presentation here</div>
  <div class="body" style="left:0;right:0;top:98px;text-align:center;color:var(--orange)">corvinex-example.com</div>
</section>

<section class="slide">
  <div class="photo" role="img" aria-label="Orange-tinted photo of an office workspace" style="inset:0;background:linear-gradient(135deg,#e4a13b,#c7852d 50%,#e9b25a)"></div>
  <div class="logo-big" style="left:65px;top:32px;font-size:15px;color:#fff">Corvinex</div>
  <div class="tagline" style="left:75px;top:52px;color:#fff;font-size:4px">People Strategy, Redefined</div>
  <div style="left:0;right:0;top:72px;text-align:center;font-size:5.5px;color:#fff">Click to include your Title Presentation</div>
  <div class="body" style="left:0;right:0;top:82px;text-align:center;color:#fff">Your Subtitle Presentation here</div>
  <div class="badge" style="right:12px;bottom:14px"></div>
</section>

<section class="slide">
  <div class="photo cool" role="img" aria-label="Photo of a team meeting around a table" style="left:0;top:0;width:104px;height:112px"></div>
  <div class="brand">Corvinex</div>
  <ol style="left:119px;top:26px;list-style:none;font-size:2.8px;line-height:4.2;color:var(--ink)">
    <li>01. <b>Opening ceremony</b></li><li>02. <b>Speakers Introduction</b></li><li>03. <b>Opening</b></li><li>04. <b>Break time</b></li><li>05. <b>Speakers</b></li><li>06. <b>Free time</b></li>
  </ol>
  <div class="footer" style="background:var(--orange)"><span></span><span style="color:#fff">www.corvinex-example.com | 5</span></div>
</section>

<!-- Row 2 -->
<section class="slide">
  <div class="brand" style="left:16px;right:auto">Corvinex</div>
  <div class="title" style="top:33px">Our <span class="accent">Vision</span></div>
  <div class="sub" style="left:15px;top:45px">Subtitle</div>
  <p class="body" style="left:15px;top:50px;width:80px">Lorem ipsum is simply dummy text of the printing and typesetting industry. It has been the standard dummy text ever since the early days, when an unknown printer took a galley of type and scrambled it to make a type specimen book that survived many decades and later moved into electronic typesetting with little change.</p>
  <div class="photo warm" role="img" aria-label="Photo of a cafe table with cups" style="left:104px;top:0;width:103px;height:112px"></div>
  <div style="left:112px;top:14px;width:72px;display:flex;flex-direction:column;gap:9px">
    <div style="background:rgba(255,255,255,.88);padding:2px;font-size:2.6px"><b>Our Vision Title</b><p class="body">A peep at some distant orb has power to raise and purify our thoughts.</p></div>
    <div style="background:rgba(255,255,255,.88);padding:2px;font-size:2.6px"><b>Our Vision Title</b><p class="body">A peep at some distant orb has power to raise and purify our thoughts.</p></div>
    <div style="background:rgba(255,255,255,.88);padding:2px;font-size:2.6px"><b>Our Vision Title</b><p class="body">A peep at some distant orb has power to raise and purify our thoughts.</p></div>
  </div>
  <div class="footer"><span>Confidential - Not for Distribution</span><span class="site">www.corvinex-example.com | 6</span></div>
</section>

<section class="slide">
  <div class="brand">Corvinex</div>
  <div class="title">Our <span class="accent">Mission</span></div>
  <div class="sub" style="left:15px;top:26px">Subtitle</div>
  <p class="body" style="left:15px;top:31px;width:178px">Lorem ipsum is simply dummy text of the printing and typesetting industry. It has been the standard dummy text ever since the early days, when an unknown printer took a galley of type and scrambled it to make a type specimen book. It survived five centuries and the leap into electronic typesetting, remaining essentially unchanged and popular.</p>
  <div class="photo cool" role="img" aria-label="Photo of people at a meeting desk" style="left:0;top:58px;width:207px;height:54px"></div>
  <div style="left:35px;top:64px;width:160px;display:flex;gap:6px">
    <div style="flex:1;background:#fff;padding:2px;font-size:2.4px"><b>Our Mission Title</b><p class="body">A peep at some distant orb has power to raise and purify.</p></div>
    <div style="flex:1;background:#fff;padding:2px;font-size:2.4px"><b>Our Mission Title</b><p class="body">A peep at some distant orb has power to raise and purify.</p></div>
    <div style="flex:1;background:#fff;padding:2px;font-size:2.4px"><b>Our Mission Title</b><p class="body">A peep at some distant orb has power to raise and purify.</p></div>
  </div>
  <div class="footer"><span>Confidential - Not for Distribution</span><span class="site">www.corvinex-example.com | 7</span></div>
</section>

<section class="slide">
  <div class="photo warm" role="img" aria-label="Photo of a woman working at a laptop" style="inset:0"></div>
  <div class="orange-panel" style="left:17px;top:0;width:82px;height:116px"></div>
  <div class="cover-title" style="left:22px;top:26px;width:74px;font-size:5.6px">Brivanta Rapid Deployment for Halvexa HR Suite</div>
  <p class="body" style="left:22px;top:66px;width:72px;color:#fff">Brivanta offers a rapid deployment of the HR suite to address your most critical talent needs, with a proven approach built for fast results and smooth adoption across your business.</p>
  <div class="orange-panel" style="left:148px;top:57px;width:42px;height:28px;font-size:3.3px;padding:3px 4px;line-height:1.5">Accelerated Journey to the Cloud</div>
  <div style="left:150px;top:96px;width:6px;height:6px;background:var(--orange)"></div>
  <div class="brand" style="color:var(--ink)">Corvinex</div>
</section>

<section class="slide">
  <div class="photo" role="img" aria-label="Photo of a student with headphones studying" style="inset:0"></div>
  <div class="orange-panel" style="left:104px;top:0;width:82px;height:116px"></div>
  <div class="brand light" style="right:24px;top:10px">Corvinex</div>
  <div class="cover-title" style="left:109px;top:28px;width:72px;font-size:5.6px">Trellana Learning Experience Platform</div>
  <p class="body" style="left:109px;top:53px;width:72px;color:#fff">Trellana is an award winning extension that brings content, people and data together in one place, creating a personalised and engaging learning experience that helps every employee grow.</p>
  <div class="orange-panel" style="left:17px;top:58px;width:40px;height:28px;font-size:3.1px;padding:3px 4px;line-height:1.5">Streaming-style Learning Experience</div>
  <div style="left:15px;top:98px;width:7px;height:7px;background:var(--orange)"></div>
</section>

<section class="slide">
  <div class="title" style="top:12px">Right Image &amp; Bullets</div>
  <div style="left:16px;top:30px;display:flex;flex-direction:column;gap:9px">
    <div class="bullet-row"><div class="dot orange">✓</div><div><div class="label">Subtitle here</div><p class="body" style="width:40px">A peep at some distant orb has power to raise and purify.</p></div></div>
    <div class="bullet-row"><div class="dot dark">✓</div><div><div class="label muted">Subtitle here</div><p class="body" style="width:40px">A peep at some distant orb has power to raise and purify.</p></div></div>
    <div class="bullet-row"><div class="dot grey">✓</div><div><div class="label muted">Subtitle here</div><p class="body" style="width:40px">A peep at some distant orb has power to raise and purify.</p></div></div>
  </div>
  <div class="photo warm" role="img" aria-label="Photo of a smiling woman with earphones" style="left:112px;top:0;width:95px;height:112px"></div>
  <div class="brand light">Corvinex</div>
  <div class="footer"><span>Confidential - Not for Distribution</span><span class="site">www.corvinex-example.com | 10</span></div>
</section>

<!-- Row 3 -->
<section class="slide">
  <div class="photo warm" role="img" aria-label="Photo of two colleagues smiling" style="left:17px;top:0;width:86px;height:112px"></div>
  <div class="brand">Corvinex</div>
  <div style="left:118px;top:20px;font-size:6.5px;line-height:1.1">Left Image<br><span class="accent">&amp; text Slide</span></div>
  <div class="sub" style="left:118px;top:42px">Subtitle</div>
  <p class="body" style="left:118px;top:47px;width:76px">Lorem ipsum is simply dummy text of the printing and typesetting industry. It has been the standard dummy text ever since the early days, when an unknown printer took a galley of type and scrambled it to make a type specimen book that survived many decades with little change.</p>
  <div class="footer"><span>Confidential - Not for Distribution</span><span class="site">www.corvinex-example.com | 11</span></div>
</section>

<section class="slide">
  <div class="brand">Corvinex</div>
  <div class="title">Our 4 <span class="accent">Services</span></div>
  <div class="sub" style="left:15px;top:38px">Subtitle</div>
  <p class="body" style="left:15px;top:43px;width:80px">Lorem ipsum is simply dummy text of the printing and typesetting industry. It has been the standard dummy text ever since the early days, when an unknown printer took a galley of type and scrambled it to make a type specimen book that survived many decades with little change.</p>
  <div style="left:113px;top:27px;width:80px;display:grid;grid-template-columns:1fr 1fr;gap:2px">
    <div class="card"><i class="icon"></i><span class="name">Subtitle here</span><p class="body">like a strain of music</p></div>
    <div class="card"><i class="icon"></i><span class="name">Subtitle here</span><p class="body">like a strain of music</p></div>
    <div class="card"><i class="icon"></i><span class="name">Subtitle here</span><p class="body">like a strain of music</p></div>
    <div class="card"><i class="icon"></i><span class="name">Subtitle here</span><p class="body">like a strain of music</p></div>
  </div>
  <div class="footer"><span>Confidential - Not for Distribution</span><span class="site">www.corvinex-example.com | 12</span></div>
</section>

<section class="slide">
  <div class="brand">Corvinex</div>
  <div class="title">Our 6 <span class="accent">Services</span></div>
  <div class="sub" style="left:15px;top:28px">Subtitle</div>
  <p class="body" style="left:15px;top:33px;width:58px">Lorem ipsum is simply dummy text of the printing and typesetting industry. It has been the standard dummy text ever since the early days, when an unknown printer took a galley of type and scrambled it to make a type specimen book that survived many decades with little change.</p>
  <div style="left:83px;top:27px;width:114px;display:grid;grid-template-columns:repeat(3,1fr);gap:2px">
    <div class="card"><i class="icon"></i><span class="name">Subtitle here</span><p class="body">like a strain of music</p></div>
    <div class="card"><i class="icon"></i><span class="name">Subtitle here</span><p class="body">like a strain of music</p></div>
    <div class="card"><i class="icon"></i><span class="name">Subtitle here</span><p class="body">like a strain of music</p></div>
    <div class="card"><i class="icon"></i><span class="name">Subtitle here</span><p class="body">like a strain of music</p></div>
    <div class="card"><i class="icon"></i><span class="name">Subtitle here</span><p class="body">like a strain of music</p></div>
    <div class="card"><i class="icon"></i><span class="name">Subtitle here</span><p class="body">like a strain of music</p></div>
  </div>
  <div class="footer"><span>Confidential - Not for Distribution</span><span class="site">www.corvinex-example.com | 13</span></div>
</section>

<section class="slide">
  <div class="brand">Corvinex</div>
  <div class="title">Our 8 <span class="accent">Services</span></div>
  <div class="sub" style="left:15px;top:28px">Subtitle</div>
  <p class="body" style="left:15px;top:33px;width:40px">Lorem ipsum is simply dummy text of the printing and typesetting industry. It has been the standard dummy text ever since the early days, when an unknown printer took a galley of type and scrambled it.</p>
  <div style="left:59px;top:29px;width:138px;display:grid;grid-template-columns:repeat(4,1fr);gap:2px">
    <div class="card"><i class="icon"></i><span class="name">Subtitle here</span><p class="body">like a strain of music</p></div>
    <div class="card"><i class="icon"></i><span class="name">Subtitle here</span><p class="body">like a strain of music</p></div>
    <div class="card"><i class="icon"></i><span class="name">Subtitle here</span><p class="body">like a strain of music</p></div>
    <div class="card"><i class="icon"></i><span class="name">Subtitle here</span><p class="body">like a strain of music</p></div>
    <div class="card"><i class="icon"></i><span class="name">Subtitle here</span><p class="body">like a strain of music</p></div>
    <div class="card"><i class="icon"></i><span class="name">Subtitle here</span><p class="body">like a strain of music</p></div>
    <div class="card"><i class="icon"></i><span class="name">Subtitle here</span><p class="body">like a strain of music</p></div>
    <div class="card"><i class="icon"></i><span class="name">Subtitle here</span><p class="body">like a strain of music</p></div>
  </div>
  <div class="footer"><span>Confidential - Not for Distribution</span><span class="site">www.corvinex-example.com | 14</span></div>
</section>

<section class="slide">
  <div class="brand">Corvinex</div>
  <div class="title">What <span class="accent">we do</span></div>
  <div class="sub" style="left:15px;top:32px">Subtitle</div>
  <p class="body" style="left:15px;top:37px;width:56px">Lorem ipsum is simply dummy text of the printing and typesetting industry. It has been the standard dummy text ever since the early days, when an unknown printer took a galley of type and scrambled it to make a type specimen book that survived many decades with little change.</p>
  <div style="left:88px;top:30px;width:108px;height:70px;display:grid;grid-template-columns:repeat(3,1fr);gap:3px">
    <div class="card"><i class="icon"></i><span class="name">Subtitle here</span><p class="body">like a strain of music, a noble picture, a passage.</p></div>
    <div class="card"><i class="icon"></i><span class="name">Subtitle here</span><p class="body">like a strain of music, a noble picture, a passage.</p></div>
    <div class="card"><i class="icon"></i><span class="name">Subtitle here</span><p class="body">like a strain of music, a noble picture, a passage.</p></div>
  </div>
  <div class="footer"><span>Confidential - Not for Distribution</span><span class="site">www.corvinex-example.com | 15</span></div>
</section>

<!-- Row 4 -->
<section class="slide">
  <div class="brand">Corvinex</div>
  <div class="title">What <span class="accent">we do</span></div>
  <div class="sub" style="left:15px;top:32px">Subtitle</div>
  <p class="body" style="left:15px;top:37px;width:47px">Lorem ipsum is simply dummy text of the printing and typesetting industry. It has been the standard dummy text ever since the early days, when an unknown printer took a galley of type and scrambled it to make a type specimen book.</p>
  <div style="left:67px;top:30px;width:132px;height:70px;display:grid;grid-template-columns:repeat(4,1fr);gap:2px">
    <div class="card"><i class="icon"></i><span class="name">Subtitle here</span><p class="body">like a strain of music, a noble picture.</p></div>
    <div class="card"><i class="icon"></i><span class="name">Subtitle here</span><p class="body">like a strain of music, a noble picture.</p></div>
    <div class="card"><i class="icon"></i><span class="name">Subtitle here</span><p class="body">like a strain of music, a noble picture.</p></div>
    <div class="card"><i class="icon"></i><span class="name">Subtitle here</span><p class="body">like a strain of music, a noble picture.</p></div>
  </div>
  <div class="footer"><span>Confidential - Not for Distribution</span><span class="site">www.corvinex-example.com | 16</span></div>
</section>

<section class="slide">
  <div class="brand">Corvinex</div>
  <div class="title">Bullet three <span class="accent">Column Slide</span></div>
  <div style="left:15px;top:28px;width:180px;display:grid;grid-template-columns:repeat(3,1fr);gap:3px">
    <div class="card" style="align-items:flex-start;text-align:left;height:70px"><div class="col-head">Bullet points &amp;<br>Title here</div><p class="body">• Like a strain of sacred music, or a noble picture.<br>• It always does one good.<br>• All their equipment and instruments are alive.<br>• A peep at some distant orb.</p></div>
    <div class="card" style="align-items:flex-start;text-align:left;height:70px"><div class="col-head">Bullet points &amp;<br>Title here</div><p class="body">• Like a strain of sacred music, or a noble picture.<br>• It always does one good.<br>• All their equipment and instruments are alive.<br>• A peep at some distant orb.</p></div>
    <div class="card" style="align-items:flex-start;text-align:left;height:70px"><div class="col-head">Bullet points &amp;<br>Title here</div><p class="body">• Like a strain of sacred music, or a noble picture.<br>• It always does one good.<br>• All their equipment and instruments are alive.<br>• A peep at some distant orb.</p></div>
  </div>
  <div class="footer"><span>Confidential - Not for Distribution</span><span class="site">www.corvinex-example.com | 17</span></div>
</section>

<section class="slide">
  <div class="brand">Corvinex</div>
  <div class="title">Bullet Four <span class="accent">column Slide</span></div>
  <div style="left:15px;top:28px;width:180px;display:grid;grid-template-columns:repeat(4,1fr);gap:2px">
    <div class="card" style="align-items:flex-start;text-align:left;height:70px"><div class="col-head">Bullet points &amp;<br>Title here</div><p class="body">• Like a strain of sacred music.<br>• It always does one good.<br>• All their equipment is alive.</p></div>
    <div class="card" style="align-items:flex-start;text-align:left;height:70px"><div class="col-head">Bullet points &amp;<br>Title here</div><p class="body">• Like a strain of sacred music.<br>• It always does one good.<br>• All their equipment is alive.</p></div>
    <div class="card" style="align-items:flex-start;text-align:left;height:70px"><div class="col-head">Bullet points &amp;<br>Title here</div><p class="body">• Like a strain of sacred music.<br>• It always does one good.<br>• All their equipment is alive.</p></div>
    <div class="card" style="align-items:flex-start;text-align:left;height:70px"><div class="col-head">Bullet points &amp;<br>Title here</div><p class="body">• Like a strain of sacred music.<br>• It always does one good.<br>• All their equipment is alive.</p></div>
  </div>
  <div class="footer"><span>Confidential - Not for Distribution</span><span class="site">www.corvinex-example.com | 18</span></div>
</section>

<section class="slide">
  <div class="brand">Corvinex</div>
  <div class="title">What <span class="accent">we do</span></div>
  <div class="sub" style="left:15px;top:28px">Subtitle</div>
  <p class="body" style="left:15px;top:33px;width:58px">Lorem ipsum is simply dummy text of the printing and typesetting industry. It has been the standard dummy text ever since the early days, when an unknown printer took a galley of type and scrambled it to make a type specimen book that survived many decades with little change.</p>
  <div style="left:98px;top:28px;display:flex;flex-direction:column;gap:5px">
    <div class="bullet-row"><div class="dot dark">✓</div><div><div class="label" style="color:var(--ink)">Subtitle here</div><p class="body" style="width:80px">A peep at some distant orb has power to raise and purify our thoughts.</p></div></div>
    <div class="bullet-row"><div class="dot orange">✓</div><div><div class="label">Subtitle here</div><p class="body" style="width:80px">A peep at some distant orb has power to raise and purify our thoughts.</p></div></div>
    <div class="bullet-row"><div class="dot grey">✓</div><div><div class="label muted">Subtitle here</div><p class="body" style="width:80px">A peep at some distant orb has power to raise and purify our thoughts.</p></div></div>
    <div class="bullet-row"><div class="dot grey">✓</div><div><div class="label muted">Subtitle here</div><p class="body" style="width:80px">A peep at some distant orb has power to raise and purify our thoughts.</p></div></div>
  </div>
  <div class="footer"><span>Confidential - Not for Distribution</span><span class="site">www.corvinex-example.com | 19</span></div>
</section>

<section class="slide">
  <div class="brand">Corvinex</div>
  <div class="title">What <span class="accent">we do</span></div>
  <div style="left:15px;top:30px;width:180px;display:grid;grid-template-columns:1fr 1fr;gap:7px 14px">
    <div class="bullet-row"><div class="dot orange">✓</div><div><div class="label">Subtitle here</div><p class="body">A peep at some distant orb has power to raise and purify our thoughts.</p></div></div>
    <div class="bullet-row"><div class="dot dark">✓</div><div><div class="label muted">Subtitle here</div><p class="body">A peep at some distant orb has power to raise and purify our thoughts.</p></div></div>
    <div class="bullet-row"><div class="dot grey">✓</div><div><div class="label muted">Subtitle here</div><p class="body">A peep at some distant orb has power to raise and purify our thoughts.</p></div></div>
    <div class="bullet-row"><div class="dot grey">✓</div><div><div class="label muted">Subtitle here</div><p class="body">A peep at some distant orb has power to raise and purify our thoughts.</p></div></div>
    <div class="bullet-row"><div class="dot grey">✓</div><div><div class="label muted">Subtitle here</div><p class="body">A peep at some distant orb has power to raise and purify our thoughts.</p></div></div>
    <div class="bullet-row"><div class="dot grey">✓</div><div><div class="label muted">Subtitle here</div><p class="body">A peep at some distant orb has power to raise and purify our thoughts.</p></div></div>
  </div>
  <div class="footer"><span>Confidential - Not for Distribution</span><span class="site">www.corvinex-example.com | 20</span></div>
</section>

<!-- Row 5 -->
<section class="slide">
  <div style="left:9px;top:10px;width:190px;height:98px;display:grid;grid-template-columns:repeat(4,1fr);grid-template-rows:1fr 1fr;gap:3px">
    <div class="photo warm" role="img" aria-label="Photo of a team at work"></div>
    <div style="background:#111;color:#fff;padding:3px"><div style="font-size:4px;font-weight:700">Corvinex</div><div class="sub" style="color:#fff;margin-top:3px">Subtitle</div><p class="body" style="color:#fff">Lorem ipsum is simply dummy text of the printing industry.</p></div>
    <div class="photo cool" role="img" aria-label="Photo of colleagues talking"></div>
    <div class="photo" role="img" aria-label="Photo of a team discussion"></div>
    <div class="photo cool" role="img" aria-label="Photo of a handshake at a desk"></div>
    <div class="photo warm" role="img" aria-label="Photo of people at a laptop"></div>
    <div class="photo cool" role="img" aria-label="Photo of a meeting room"></div>
    <div class="photo" role="img" aria-label="Photo of a group working together"></div>
  </div>
  <div class="footer"><span>Confidential - Not for Distribution</span><span class="site">www.corvinex-example.com | 21</span></div>
</section>

<section class="slide">
  <div class="photo warm" role="img" aria-label="Photo of a business meeting" style="left:0;top:0;width:72px;height:112px"></div>
  <div style="left:4px;top:80px;font-size:5.5px;color:#fff;line-height:1.1">Some of our<br>Customers Are</div>
  <div class="brand">Corvinex</div>
  <div style="left:80px;top:14px;width:98px;display:grid;grid-template-columns:repeat(4,1fr);gap:9px 8px">
    <i style="height:8px;border-radius:50%;background:#f3a445;width:8px;margin:auto"></i><i style="height:5px;background:#d33"></i><i style="height:7px;background:#3a6fb0"></i><i style="height:8px;width:8px;border-radius:50%;background:#e22;margin:auto"></i>
    <i style="height:6px;background:#2a55a0"></i><i style="height:8px;width:8px;border-radius:50%;background:#2a8a4a;margin:auto"></i><i style="height:5px;background:#111"></i><i style="height:6px;background:#e8552b"></i>
    <i style="height:6px;background:#c33"></i><i style="height:8px;width:8px;border-radius:50%;background:#8cc63f;margin:auto"></i><i style="height:6px;background:#c22"></i><i style="height:5px;background:#555"></i>
    <i style="height:7px;width:7px;background:#f5c000;margin:auto"></i><i style="height:6px;background:#3b7fc4"></i><i style="height:5px;background:#d33"></i><i style="height:4px;background:#222"></i>
  </div>
  <div class="footer"><span></span><span class="site">www.corvinex-example.com | 22</span></div>
</section>

<section class="slide">
  <div class="brand">Corvinex</div>
  <div class="title">What <span class="accent">We Do</span></div>
  <div style="left:18px;top:28px;width:175px;display:grid;grid-template-columns:repeat(3,1fr);gap:9px 10px">
    <div><i style="width:5px;height:5px;border:0.6px solid var(--orange);border-radius:50%;display:block"></i><div style="font-size:2.6px;color:var(--orange)">Lorem dummy text</div><p class="body">Lorem ipsum is simply dummy text of the printing industry.</p></div>
    <div><i style="width:5px;height:5px;border:0.6px solid var(--orange);border-radius:50%;display:block"></i><div style="font-size:2.6px;color:var(--orange)">Lorem dummy text</div><p class="body">Lorem ipsum is simply dummy text of the printing industry.</p></div>
    <div><i style="width:5px;height:5px;border:0.6px solid var(--orange);border-radius:50%;display:block"></i><div style="font-size:2.6px;color:var(--orange)">Lorem dummy text</div><p class="body">Lorem ipsum is simply dummy text of the printing industry.</p></div>
    <div><i style="width:5px;height:5px;border:0.6px solid var(--orange);border-radius:50%;display:block"></i><div style="font-size:2.6px;color:var(--orange)">Lorem dummy text</div><p class="body">Lorem ipsum is simply dummy text of the printing industry.</p></div>
    <div><i style="width:5px;height:5px;border:0.6px solid var(--orange);border-radius:50%;display:block"></i><div style="font-size:2.6px;color:var(--orange)">Lorem dummy text</div><p class="body">Lorem ipsum is simply dummy text of the printing industry.</p></div>
    <div><i style="width:5px;height:5px;border:0.6px solid var(--orange);border-radius:50%;display:block"></i><div style="font-size:2.6px;color:var(--orange)">Lorem dummy text</div><p class="body">Lorem ipsum is simply dummy text of the printing industry.</p></div>
  </div>
  <div class="footer"><span>Confidential - Not for Distribution</span><span class="site">www.corvinex-example.com | 23</span></div>
</section>

<section class="slide">
  <div class="brand">Corvinex</div>
  <div class="title">Click to edit <span class="accent">title slide</span></div>
  <div style="left:16px;top:30px;width:176px;display:grid;grid-template-columns:repeat(3,1fr);grid-template-rows:repeat(2,30px);gap:2px">
    <div class="orange-panel" style="padding:3px"><div style="font-size:2.8px">Title</div><p class="body" style="color:#fff;margin-top:3px">Lorem Ipsum is simply dummy text of the printing industry.</p></div>
    <div style="background:#f4f4f4;padding:3px"><div style="font-size:2.8px">Title</div><p class="body" style="margin-top:3px">Lorem Ipsum is simply dummy text of the printing industry.</p></div>
    <div style="background:#f4f4f4;padding:3px"><div style="font-size:2.8px">Title</div><p class="body" style="margin-top:3px">Lorem Ipsum is simply dummy text of the printing industry.</p></div>
    <div style="background:#f4f4f4;padding:3px"><div style="font-size:2.8px">Title</div><p class="body" style="margin-top:3px">Lorem Ipsum is simply dummy text of the printing industry.</p></div>
    <div style="background:#f4f4f4;padding:3px"><div style="font-size:2.8px">Title</div><p class="body" style="margin-top:3px">Lorem Ipsum is simply dummy text of the printing industry.</p></div>
    <div style="background:#f4f4f4;padding:3px"><div style="font-size:2.8px">Title</div><p class="body" style="margin-top:3px">Lorem Ipsum is simply dummy text of the printing industry.</p></div>
  </div>
  <div class="footer"><span>Confidential - Not for Distribution</span><span class="site">www.corvinex-example.com | 24</span></div>
</section>

<section class="slide">
  <div class="brand">Corvinex</div>
  <div class="title">Our <span class="accent">services</span></div>
  <div style="left:16px;top:29px;width:178px;display:grid;grid-template-columns:repeat(3,1fr);gap:7px 8px;text-align:center">
    <div><i class="dot orange" style="margin:0 auto;display:block"></i><div style="font-size:2.6px;margin-top:1px">Lorem dummy text</div><p class="body">Lorem Ipsum is simply dummy text of the printing industry.</p></div>
    <div><i class="dot orange" style="margin:0 auto;display:block"></i><div style="font-size:2.6px;margin-top:1px">Lorem dummy text</div><p class="body">Lorem Ipsum is simply dummy text of the printing industry.</p></div>
    <div><i class="dot orange" style="margin:0 auto;display:block"></i><div style="font-size:2.6px;margin-top:1px">Lorem dummy text</div><p class="body">Lorem Ipsum is simply dummy text of the printing industry.</p></div>
    <div><i class="dot orange" style="margin:0 auto;display:block"></i><div style="font-size:2.6px;margin-top:1px">Lorem dummy text</div><p class="body">Lorem Ipsum is simply dummy text of the printing industry.</p></div>
    <div><i class="dot orange" style="margin:0 auto;display:block"></i><div style="font-size:2.6px;margin-top:1px">Lorem dummy text</div><p class="body">Lorem Ipsum is simply dummy text of the printing industry.</p></div>
    <div><i class="dot orange" style="margin:0 auto;display:block"></i><div style="font-size:2.6px;margin-top:1px">Lorem dummy text</div><p class="body">Lorem Ipsum is simply dummy text of the printing industry.</p></div>
  </div>
  <div class="footer"><span>Confidential - Not for Distribution</span><span class="site">www.corvinex-example.com | 25</span></div>
</section>

<!-- Row 6 -->
<section class="slide">
  <div class="brand">Corvinex</div>
  <div class="title">Click to edit <span class="accent">title slide</span></div>
  <div style="left:20px;top:38px;width:170px;display:grid;grid-template-columns:repeat(3,1fr);gap:10px">
    <div><div style="font-size:2.6px;color:var(--orange)">Lorem dummy text</div><div class="photo warm" role="img" aria-label="Photo of a woman at a laptop" style="height:22px;margin:4px 0"></div><p class="body">Lorem Ipsum is simply dummy text of the printing industry.</p></div>
    <div><div style="font-size:2.6px;color:var(--orange)">Lorem dummy text</div><div class="photo cool" role="img" aria-label="Photo of a man in an office" style="height:22px;margin:4px 0"></div><p class="body">Lorem Ipsum is simply dummy text of the printing industry.</p></div>
    <div><div style="font-size:2.6px;color:var(--orange)">Lorem dummy text</div><div class="photo" role="img" aria-label="Photo of a woman working" style="height:22px;margin:4px 0"></div><p class="body">Lorem Ipsum is simply dummy text of the printing industry.</p></div>
  </div>
  <div class="footer"><span>Confidential - Not for Distribution</span><span class="site">www.corvinex-example.com | 26</span></div>
</section>

<section class="slide">
  <div class="brand">Corvinex</div>
  <div class="title">Our Core <span class="accent">Services</span></div>
  <div class="sub" style="left:15px;top:28px">Subtitle</div>
  <p class="body" style="left:15px;top:33px;width:60px">Lorem ipsum is simply dummy text of the printing and typesetting industry. It has been the standard dummy text ever since the early days, when an unknown printer took a galley of type and scrambled it to make a type specimen book that survived many decades with little change.</p>
  <svg style="left:88px;top:10px" width="100" height="100" viewBox="0 0 100 100">
    <g opacity=".82"><circle cx="50" cy="30" r="21" fill="#f39a2a"/><circle cx="70" cy="52" r="21" fill="#f5b43a"/><circle cx="50" cy="74" r="21" fill="#e9b21e"/><circle cx="30" cy="52" r="21" fill="#7d7468"/></g>
    <g font-family="Lato,sans-serif" font-size="2.6" fill="#fff" text-anchor="middle"><text x="50" y="22">Marketing</text><text x="74" y="52">Creative Design</text><text x="50" y="86">Photography</text><text x="26" y="52">Motion Design</text></g>
  </svg>
  <div class="footer"><span>Confidential - Not for Distribution</span><span class="site">www.corvinex-example.com | 27</span></div>
</section>

<section class="slide">
  <div class="brand">Corvinex</div>
  <svg style="left:60px;top:14px" width="86" height="86" viewBox="0 0 86 86">
    <circle cx="43" cy="43" r="38" fill="none" stroke="#222" stroke-width=".8"/>
    <circle cx="43" cy="43" r="26" fill="#e2a33a"/>
    <circle cx="43" cy="43" r="20" fill="#8a6e52"/>
    <circle cx="43" cy="17" r="3.5" fill="#f7941d"/><circle cx="69" cy="43" r="3.5" fill="#f7941d"/><circle cx="43" cy="69" r="3.5" fill="#f7941d"/><circle cx="17" cy="43" r="3.5" fill="#f7941d"/>
  </svg>
  <div style="left:38px;top:42px;font-size:3.2px;text-align:right">Social media<br>Design</div>
  <div style="left:150px;top:42px;font-size:3.2px">Creative<br>Design</div>
  <div style="left:52px;top:82px;font-size:3.2px">UI/UX<br>Design</div>
  <div style="left:148px;top:82px;font-size:3.2px">Motion &amp;<br>Video<br>Design</div>
  <div class="footer"><span>Confidential - Not for Distribution</span><span class="site">www.corvinex-example.com | 28</span></div>
</section>

<section class="slide">
  <div class="brand">Corvinex</div>
  <div class="title">What <span class="accent">we do</span></div>
  <div class="sub" style="left:15px;top:24px">Subtitle</div>
  <p class="body" style="left:15px;top:29px;width:178px">Lorem ipsum is simply dummy text of the printing and typesetting industry. It has been the standard dummy text ever since the early days, when an unknown printer took a galley of type.</p>
  <div style="left:20px;top:44px;width:170px;height:56px;display:grid;grid-template-columns:repeat(4,1fr);gap:4px;align-items:center;text-align:center">
    <div><div style="font-size:2.6px">Step - 1</div><p class="body">Apparently we had reached a great height in the atmosphere.</p></div>
    <div class="orange-panel" style="height:56px;padding:4px 2px"><div style="font-size:2.6px">Step - 2</div><p class="body" style="color:#fff">By the same illusion which lifts the horizon of the sea to the level of the spectator.</p></div>
    <div><div style="font-size:2.6px">Step - 3</div><p class="body">Same illusion which lifts the horizon of the sea.</p></div>
    <div><div style="font-size:2.6px">Step - 4</div><p class="body">When again we rose above the clouds.</p></div>
  </div>
  <div class="footer"><span>Confidential - Not for Distribution</span><span class="site">www.corvinex-example.com | 29</span></div>
</section>

<section class="slide">
  <div class="brand">Corvinex</div>
  <div class="title">Our <span class="accent">Solutions</span></div>
  <svg style="left:22px;top:28px" width="70" height="80" viewBox="0 0 70 80">
    <path d="M20 42 L52 10 M20 42 L40 35 M20 42 L52 60 M20 42 L40 80" stroke="#f7941d" stroke-width=".5" fill="none"/>
    <circle cx="20" cy="42" r="13" fill="#9a7f66"/>
    <circle cx="52" cy="11" r="9" fill="#f7941d"/><circle cx="42" cy="34" r="7" fill="#f5a623"/><circle cx="52" cy="58" r="8" fill="#f7941d"/><circle cx="40" cy="72" r="7" fill="#f5b400"/>
    <g font-family="Lato,sans-serif" font-size="2.3" fill="#fff" text-anchor="middle"><text x="52" y="12">Solution 01</text><text x="42" y="35">Solution 02</text><text x="52" y="59">Solution 03</text><text x="40" y="73">Solution 04</text></g>
  </svg>
  <div style="left:104px;top:32px;width:92px;display:flex;flex-direction:column;gap:10px">
    <p class="body">Apparently we had reached a great height in the atmosphere.</p>
    <p class="body">Apparently we had reached a great height, for the sky was a dead black.</p>
    <p class="body">By the same illusion which lifts the horizon of the sea to the level of the spectator.</p>
    <p class="body">Apparently we had reached a great height in the atmosphere.</p>
  </div>
  <div class="footer"><span>Confidential - Not for Distribution</span><span class="site">www.corvinex-example.com | 30</span></div>
</section>

<!-- Row 7 -->
<section class="slide">
  <div class="brand">Corvinex</div>
  <div class="title center" style="top:14px">Business Plan</div>
  <div class="kicker" style="left:0;top:24px;text-align:center">LOREM IPSUM, GIVING INFORMATION ON ITS ORIGINS, AS WELL AS A RANDOM TEXT HERE</div>
  <div style="left:17px;top:33px;display:flex">
    <div class="ring" style="width:38px;height:38px;background:#f5a03a;color:#fff">Title</div>
    <div class="ring" style="width:38px;height:38px;background:#eeaa26;color:#fff;margin-left:-4px">Title</div>
    <div class="ring" style="width:38px;height:38px;background:#e0b21a;color:#fff;margin-left:-4px">Title</div>
    <div class="ring" style="width:38px;height:38px;background:#d4a42a;color:#fff;margin-left:-4px">Title</div>
    <div class="ring" style="width:38px;height:38px;background:#b98466;color:#fff;margin-left:-4px">Title</div>
  </div>
  <div style="left:17px;top:76px;width:174px;display:grid;grid-template-columns:repeat(5,1fr);text-align:center;gap:3px">
    <p class="body">Lorem ipsum dolor sit amet, consectetur elit.</p><p class="body">Lorem ipsum dolor sit amet, consectetur elit.</p><p class="body">Lorem ipsum dolor sit amet, consectetur elit.</p><p class="body">Lorem ipsum dolor sit amet, consectetur elit.</p><p class="body">Lorem ipsum dolor sit amet, consectetur elit.</p>
  </div>
  <div class="footer"><span>Confidential - Not for Distribution</span><span class="site">www.corvinex-example.com | 31</span></div>
</section>

<section class="slide">
  <div class="brand">Corvinex</div>
  <div class="title center">One column <span class="accent">text Slide</span></div>
  <div class="kicker" style="left:0;top:24px;text-align:center">LOREM IPSUM, GIVING INFORMATION ON ITS ORIGINS, AS WELL AS A RANDOM TEXT HERE</div>
  <p class="body" style="left:15px;top:31px;width:178px">Lorem ipsum is simply dummy text of the printing and typesetting industry. It has been the standard dummy text ever since the early days, when an unknown printer took a galley of type and scrambled it to make a type specimen book. It has survived five centuries and the leap into electronic typesetting. Contrary to popular belief, it is not simply random text; it has roots in classical literature, making it over two thousand years old. A professor looked up one of the more obscure words and discovered its source. Contrary to popular belief, it is not simply random text; it has roots in classical literature, making it over two thousand years old. The standard chunk used since then is reproduced below for those interested.</p>
  <div class="footer"><span>Confidential - Not for Distribution</span><span class="site">www.corvinex-example.com | 32</span></div>
</section>

<section class="slide">
  <div class="brand">Corvinex</div>
  <div class="title center">Two column <span class="accent">text Slide</span></div>
  <div class="kicker" style="left:0;top:24px;text-align:center">LOREM IPSUM, GIVING INFORMATION ON ITS ORIGINS, AS WELL AS A RANDOM TEXT HERE</div>
  <div style="left:15px;top:31px;width:178px;display:grid;grid-template-columns:1fr 1fr;gap:6px">
    <p class="body">Lorem ipsum is simply dummy text of the printing and typesetting industry. It has been the standard dummy text ever since the early days, when an unknown printer took a galley of type and scrambled it to make a type specimen book. Contrary to popular belief, it is not simply random text; it has roots in classical literature, making it over two thousand years old and still in use.</p>
    <p class="body">Lorem ipsum is simply dummy text of the printing and typesetting industry. It has been the standard dummy text ever since the early days, when an unknown printer took a galley of type and scrambled it to make a type specimen book. Contrary to popular belief, it is not simply random text; it has roots in classical literature, making it over two thousand years old and still in use.</p>
  </div>
  <div class="footer"><span>Confidential - Not for Distribution</span><span class="site">www.corvinex-example.com | 33</span></div>
</section>

<section class="slide">
  <div class="brand">Corvinex</div>
  <div class="title center">Three column <span class="accent">text Slide</span></div>
  <div class="kicker" style="left:0;top:24px;text-align:center">LOREM IPSUM, GIVING INFORMATION ON ITS ORIGINS, AS WELL AS A RANDOM TEXT HERE</div>
  <div style="left:15px;top:31px;width:178px;display:grid;grid-template-columns:repeat(3,1fr);gap:5px">
    <p class="body">Lorem ipsum is simply dummy text of the printing and typesetting industry. It has been the standard dummy text ever since the early days, when an unknown printer took a galley of type and scrambled it to make a type specimen book that lasted.</p>
    <p class="body">Lorem ipsum is simply dummy text of the printing and typesetting industry. It has been the standard dummy text ever since the early days, when an unknown printer took a galley of type and scrambled it to make a type specimen book that lasted.</p>
    <p class="body">Lorem ipsum is simply dummy text of the printing and typesetting industry. It has been the standard dummy text ever since the early days, when an unknown printer took a galley of type and scrambled it to make a type specimen book that lasted.</p>
  </div>
  <div class="footer"><span>Confidential - Not for Distribution</span><span class="site">www.corvinex-example.com | 34</span></div>
</section>

<section class="slide">
  <div class="brand">Corvinex</div>
  <div class="title center">Master Table</div>
  <div class="kicker" style="left:0;top:24px;text-align:center">LOREM IPSUM, GIVING INFORMATION ON ITS ORIGINS, AS WELL AS A RANDOM TEXT HERE</div>
  <table class="grid" style="left:16px;top:31px;width:176px">
    <tr><td></td><th>Column 1</th><th>Column 2</th><th>Column 3</th><th>Column 4</th><th>Column 5</th><th>Column 6</th></tr>
    <tr><td>Fila 01</td><td>48</td><td>66</td><td>75</td><td>45</td><td>66</td><td>34</td></tr>
    <tr><td>Fila 02</td><td>35</td><td>75</td><td>89</td><td>58</td><td>48</td><td>66</td></tr>
    <tr><td>Fila 03</td><td>66</td><td>34</td><td>55</td><td>35</td><td>35</td><td>75</td></tr>
    <tr><td>Fila 04</td><td>55</td><td>70</td><td>84</td><td>52</td><td>55</td><td>35</td></tr>
    <tr><td>Fila 05</td><td>48</td><td>66</td><td>75</td><td>45</td><td>66</td><td>34</td></tr>
    <tr><td>Fila 06</td><td>35</td><td>75</td><td>89</td><td>58</td><td>48</td><td>66</td></tr>
    <tr><td>Fila 07</td><td>66</td><td>34</td><td>55</td><td>35</td><td>35</td><td>75</td></tr>
    <tr><td>Fila 08</td><td>55</td><td>70</td><td>84</td><td>52</td><td>55</td><td>35</td></tr>
    <tr><td>Fila 09</td><td>48</td><td>66</td><td>75</td><td>45</td><td>66</td><td>34</td></tr>
    <tr><td>Total Columns</td><td>456</td><td>556</td><td>681</td><td>425</td><td>474</td><td>454</td></tr>
  </table>
  <div class="footer"><span>Confidential - Not for Distribution</span><span class="site">www.corvinex-example.com | 35</span></div>
</section>

<!-- Row 8: charts -->
<section class="slide">
  <div class="brand">Corvinex</div>
  <div class="title">Data <span class="accent">chart</span></div>
  <div class="kicker" style="top:24px">LOREM IPSUM, GIVING INFORMATION ON ITS ORIGINS, AS WELL AS A RANDOM TEXT HERE</div>
  <svg style="left:22px;top:34px" width="164" height="30" viewBox="0 0 164 30" font-family="Lato,sans-serif">
    <g fill="none" stroke-width="1.4">
      <circle cx="20" cy="15" r="10" stroke="#bbb" stroke-dasharray="31.4 62.8" transform="rotate(-90 20 15)"/>
      <circle cx="62" cy="15" r="10" stroke="#222" stroke-dasharray="18.8 62.8" transform="rotate(-90 62 15)"/>
      <circle cx="103" cy="15" r="10" stroke="#f5b400" stroke-dasharray="6.3 62.8" transform="rotate(-90 103 15)"/>
      <circle cx="145" cy="15" r="10" stroke="#f7941d" stroke-dasharray="25.1 62.8" transform="rotate(-90 145 15)"/>
    </g>
    <g font-size="4" text-anchor="middle"><text x="20" y="16.5" fill="#222">50%</text><text x="62" y="16.5" fill="#222">30%</text><text x="103" y="16.5" fill="#f5b400">10%</text><text x="145" y="16.5" fill="#f7941d">40%</text></g>
  </svg>
  <div style="left:22px;top:68px;width:164px;display:grid;grid-template-columns:repeat(4,1fr);gap:6px;text-align:center">
    <div><div style="font-size:2.4px;color:#999">Data title here</div><p class="body">A peep at some distant orb has power to raise.</p></div>
    <div><div style="font-size:2.4px;font-weight:700">Data title here</div><p class="body">A peep at some distant orb has power to raise.</p></div>
    <div><div style="font-size:2.4px;color:var(--gold)">Data title here</div><p class="body">A peep at some distant orb has power to raise.</p></div>
    <div><div style="font-size:2.4px;color:var(--orange)">Data title here</div><p class="body">A peep at some distant orb has power to raise.</p></div>
  </div>
  <div class="footer"><span>Confidential - Not for Distribution</span><span class="site">www.corvinex-example.com | 36</span></div>
</section>

<section class="slide">
  <div class="brand">Corvinex</div>
  <div class="title">Data <span class="accent">chart # 2</span></div>
  <div class="kicker" style="top:24px">LOREM IPSUM, GIVING INFORMATION ON ITS ORIGINS, AS WELL AS A RANDOM TEXT HERE</div>
  <svg style="left:16px;top:30px" width="180" height="76" viewBox="0 0 180 76" font-family="Lato,sans-serif">
    <g fill="none" stroke-width="1.6">
      <circle cx="20" cy="16" r="9" stroke="#f5b400" stroke-dasharray="5.6 56.5" transform="rotate(-90 20 16)"/>
      <circle cx="84" cy="16" r="9" stroke="#f5b400" stroke-dasharray="50.9 56.5" transform="rotate(-90 84 16)"/>
      <circle cx="151" cy="16" r="9" stroke="#222" stroke-dasharray="42.4 56.5" transform="rotate(-90 151 16)"/>
      <circle cx="43" cy="52" r="9" stroke="#f5b400" stroke-dasharray="19.8 56.5" transform="rotate(-90 43 52)"/>
      <circle cx="121" cy="52" r="9" stroke="#f7941d" stroke-dasharray="13 56.5" transform="rotate(-90 121 52)"/>
    </g>
    <g font-size="4" text-anchor="middle"><text x="20" y="17.5" fill="#f5b400">10%</text><text x="84" y="17.5" fill="#f5b400">90%</text><text x="151" y="17.5" fill="#222">75%</text><text x="43" y="53.5" fill="#f5b400">35%</text><text x="121" y="53.5" fill="#f7941d">23%</text></g>
    <g font-size="2.3" fill="#f7941d"><text x="34" y="8">Data title here</text><text x="100" y="8">Data title here</text><text x="54" y="44">Data title here</text><text x="80" y="44">Data title here</text><text x="140" y="33" fill="#222">Data title here</text></g>
    <g font-size="1.9" fill="#777"><text x="34" y="12">A peep at some distant</text><text x="100" y="12">A peep at some distant</text><text x="54" y="48">A peep at some distant</text><text x="80" y="48">A peep at some distant</text><text x="140" y="37">A peep at some distant</text></g>
  </svg>
  <div class="footer"><span>Confidential - Not for Distribution</span><span class="site">www.corvinex-example.com | 37</span></div>
</section>

<section class="slide">
  <div class="brand">Corvinex</div>
  <div class="title">Data Overview</div>
  <div class="kicker" style="top:24px">LOREM IPSUM, GIVING INFORMATION ON ITS ORIGINS, AS WELL AS A RANDOM TEXT HERE</div>
  <div class="sub" style="left:15px;top:38px;font-size:2.8px">Your Subtitle here</div>
  <p class="body" style="left:15px;top:43px;width:58px">Lorem ipsum is simply dummy text of the printing and typesetting industry. It has been the standard dummy text ever since the early days. A peep at some distant orb has power to raise and purify our thoughts like a strain of sacred music.</p>
  <svg style="left:105px;top:32px" width="80" height="72" viewBox="0 0 80 72" font-family="Lato,sans-serif">
    <path d="M42 36 L42 12 A24 24 0 1 1 25 53 Z" fill="#f5b400"/>
    <path d="M40 35 L23 52 A24 24 0 0 1 17 28 Z" fill="#f7941d"/>
    <path d="M40 34 L16 27 A24 24 0 0 1 28 13 Z" fill="#f7c08a"/>
    <path d="M40 33 L29 12 A24 24 0 0 1 40 9 Z" fill="#e88a6a"/>
    <g font-size="2.2" fill="#555"><text x="66" y="46">2016</text><text x="2" y="58">2017</text><text x="8" y="20">2018</text><text x="34" y="5">2019</text></g>
    <g font-size="2" fill="#555"><text x="16" y="70">• 2016 • 2017 • 2018 • 2019</text></g>
  </svg>
  <div class="footer"><span>Confidential - Not for Distribution</span><span class="site">www.corvinex-example.com | 38</span></div>
</section>

<section class="slide">
  <div class="brand">Corvinex</div>
  <div class="title">Data Overview</div>
  <div class="kicker" style="top:24px">LOREM IPSUM, GIVING INFORMATION ON ITS ORIGINS, AS WELL AS A RANDOM TEXT HERE</div>
  <div class="sub" style="left:15px;top:38px;font-size:2.8px">Your Subtitle here</div>
  <p class="body" style="left:15px;top:43px;width:58px">Lorem ipsum is simply dummy text of the printing and typesetting industry. It has been the standard dummy text ever since the early days. A peep at some distant orb has power to raise and purify our thoughts like a strain of sacred music.</p>
  <svg style="left:85px;top:36px" width="110" height="66" viewBox="0 0 110 66" font-family="Lato,sans-serif">
    <g stroke="#eee" stroke-width=".3"><line x1="8" y1="10" x2="108" y2="10"/><line x1="8" y1="25" x2="108" y2="25"/><line x1="8" y1="40" x2="108" y2="40"/><line x1="8" y1="55" x2="108" y2="55"/></g>
    <g fill="#f7941d"><rect x="14" y="18" width="5" height="37"/><rect x="38" y="35" width="5" height="20"/><rect x="62" y="26" width="5" height="29"/><rect x="86" y="10" width="5" height="45"/></g>
    <g fill="#f5b400"><rect x="20" y="34" width="5" height="21"/><rect x="44" y="16" width="5" height="39"/><rect x="68" y="39" width="5" height="16"/><rect x="92" y="30" width="5" height="25"/></g>
    <g fill="#b57a3a"><rect x="26" y="40" width="5" height="15"/><rect x="50" y="37" width="5" height="18"/><rect x="74" y="31" width="5" height="24"/><rect x="98" y="14" width="5" height="41"/></g>
    <g font-size="2" fill="#666" text-anchor="middle"><text x="22" y="60">Category 1</text><text x="46" y="60">Category 2</text><text x="70" y="60">Category 3</text><text x="94" y="60">Category 4</text><text x="58" y="65">• Series 1  • Series 2  • Series 3</text></g>
  </svg>
  <div class="footer"><span>Confidential - Not for Distribution</span><span class="site">www.corvinex-example.com | 39</span></div>
</section>

<section class="slide">
  <div class="brand">Corvinex</div>
  <div class="title">Stacked Bar Style</div>
  <div class="kicker" style="top:24px">LOREM IPSUM, GIVING INFORMATION ON ITS ORIGINS, AS WELL AS A RANDOM TEXT HERE</div>
  <div class="sub" style="left:15px;top:38px;font-size:2.8px">Your Subtitle here</div>
  <p class="body" style="left:15px;top:43px;width:50px">Lorem ipsum is simply dummy text of the printing and typesetting industry. A peep at some distant orb has power to raise and purify our thoughts like a strain of sacred music.</p>
  <svg style="left:78px;top:36px" width="120" height="66" viewBox="0 0 120 66" font-family="Lato,sans-serif">
    <g stroke="#eee" stroke-width=".3"><line x1="14" y1="4" x2="14" y2="56"/><line x1="40" y1="4" x2="40" y2="56"/><line x1="66" y1="4" x2="66" y2="56"/><line x1="92" y1="4" x2="92" y2="56"/></g>
    <g><rect x="14" y="7" width="30" height="3" fill="#f7941d"/><rect x="44" y="7" width="18" height="3" fill="#f5b400"/><rect x="62" y="7" width="44" height="3" fill="#e0a800"/></g>
    <g><rect x="14" y="20" width="22" height="3" fill="#f7941d"/><rect x="36" y="20" width="22" height="3" fill="#f5b400"/><rect x="58" y="20" width="20" height="3" fill="#e0a800"/></g>
    <g><rect x="14" y="33" width="35" height="3" fill="#f7941d"/><rect x="49" y="33" width="18" height="3" fill="#f5b400"/><rect x="67" y="33" width="12" height="3" fill="#e0a800"/></g>
    <g><rect x="14" y="46" width="26" height="3" fill="#f7941d"/><rect x="40" y="46" width="22" height="3" fill="#f5b400"/><rect x="62" y="46" width="14" height="3" fill="#e0a800"/></g>
    <g font-size="1.9" fill="#777"><text x="0" y="9">Category 4</text><text x="0" y="22">Category 3</text><text x="0" y="35">Category 2</text><text x="0" y="48">Category 1</text><text x="34" y="63">• Series 1  • Series 2  • Series 3</text></g>
  </svg>
  <div class="footer"><span>Confidential - Not for Distribution</span><span class="site">www.corvinex-example.com | 40</span></div>
</section>

</main>
</body>
</html>
```